BRQ, LLC Original

I need a business card design for a new company in Gaithersburg, MD. Though the name of the company is Volt Harbor Crafters (BRQ) we specialize in commercial kitchen ventilation systems as a complete turnkey project or as a service provider. We can design the entire system including the hoods, fans, ductwork, and fire system. We also specialize in fire alarm service, design, install and inspection. We are experts on any Plumeridge Systems equipment including Norvex PCU, Norvex Hoods, EMS controls, Standard controls, PCU filtration and Make-up Air units with heaters and cooling. We can repair/retrofit old water wash hood systems as well. We are experts with local code requirements and upgrades.

Industry/Entity Type

Business

Contact Information for Business Card

Dale Finnick, Volt Harbor Crafters, LLC; 555-318-0472 Cell, Gaithersburg, MD 20879. Daled@voltharborcrafters.example

```html
<!DOCTYPE html>
<html lang="en">
<head>
<meta charset="utf-8">
<title>Dale Finnick – Business Card</title>
<link href="https://fonts.googleapis.com/css2?family=Open+Sans:wght@400;600&display=swap" rel="stylesheet">
<style>
  :root {
    --ink: #58585a;
    --accent: #f5a31a;
    --paper: #ffffff;
    --stage-light: #ffffff;
    --stage-grey: #e6e7e9;
    --card-edge: #dcdcdc;
    --back-text: #ffffff;
  }
  * { margin: 0; padding: 0; box-sizing: border-box; }
  html, body { width: 1200px; height: 1000px; overflow: hidden; }
  body {
    position: relative;
    font-family: "Open Sans", sans-serif;
    background: var(--stage-grey);
  }
  .band-light {
    position: absolute; left: 0; top: 0;
    width: 1200px; height: 600px;
    background: var(--stage-light);
  }
  .band-shadow {
    position: absolute; left: 0; top: 600px;
    width: 1200px; height: 55px;
    background: radial-gradient(ellipse 58% 100% at 50% 0%, rgba(0,0,0,0.7), rgba(0,0,0,0.25) 55%, rgba(0,0,0,0) 85%);
  }
  .card-set { position: absolute; left: 204px; width: 792px; height: 218px; }
  .card-set.top { top: 191px; }
  .card-set.bottom { top: 691px; }
  .card {
    position: absolute; top: 0;
    width: 380px; height: 218px;
  }
  .card-front {
    left: 0;
    background: var(--paper);
    border: 1px solid var(--card-edge);
  }
  .card-back {
    left: 412px;
    background: var(--ink);
  }
  .brand {
    position: absolute; right: 37px; top: 122px;
    text-align: right;
  }
  .brand-name {
    font-size: 38px; font-weight: 600;
    color: var(--ink); line-height: 42px;
    letter-spacing: -0.6px;
  }
  .brand-tagline {
    font-size: 10px; font-weight: 600;
    color: var(--accent); line-height: 14px;
  }
  .contact-list {
    position: absolute; left: 30px; top: 122px;
    list-style: none;
  }
  .contact-item {
    display: flex; align-items: center;
    height: 20px;
    font-size: 15.5px; color: var(--back-text);
    letter-spacing: -0.4px;
  }
  .contact-item svg { width: 14px; height: 16px; margin-right: 13px; flex: none; }
</style>
</head>
<body>
  <div class="band-light"></div>
  <div class="band-shadow"></div>

  <div class="card-set top">
    <div class="card card-front">
      <div class="brand">
        <div class="brand-name">Dale Finnick</div>
        <div class="brand-tagline">Volt Harbor Crafters, LLC</div>
      </div>
    </div>
    <div class="card card-back">
      <ul class="contact-list">
        <li class="contact-item">
          <svg viewBox="0 0 14 16"><circle cx="7" cy="8" r="6.5" fill="#f5a31a"/><path d="M4.6 5.2c.4-.4.9-.3 1.1.1l.6 1.1c.2.3.1.6-.2.8l-.3.3c.4.9 1 1.5 1.9 1.9l.3-.3c.2-.3.5-.4.8-.2l1.1.6c.4.2.5.7.1 1.1-.7.8-1.6.8-2.6.2-1.2-.7-2.3-1.8-3-3-.6-1-.6-1.9.2-2.6z" fill="#58585a"/></svg>
          555-318-0472
        </li>
        <li class="contact-item">
          <svg viewBox="0 0 14 16"><path d="M7 1a5 5 0 0 0-5 5c0 3.5 5 9 5 9s5-5.5 5-9a5 5 0 0 0-5-5z" fill="none" stroke="#f5a31a" stroke-width="2"/></svg>
          Brookvale MD 20911
        </li>
        <li class="contact-item">
          <svg viewBox="0 0 14 16"><rect x="0.5" y="4" width="13" height="9" fill="#f5a31a"/><path d="M0.5 4.5 7 9.5 13.5 4.5" fill="none" stroke="#58585a" stroke-width="1"/></svg>
          Daled@voltharborcrafters.example
        </li>
      </ul>
    </div>
  </div>

  <div class="card-set bottom">
    <div class="card card-front">
      <div class="brand">
        <div class="brand-name">Dale Finnick</div>
        <div class="brand-tagline">Volt Harbor Crafters, LLC</div>
      </div>
    </div>
    <div class="card card-back">
      <ul class="contact-list">
        <li class="contact-item">
          <svg viewBox="0 0 14 16"><circle cx="7" cy="8" r="6.5" fill="#f5a31a"/><path d="M4.6 5.2c.4-.4.9-.3 1.1.1l.6 1.1c.2.3.1.6-.2.8l-.3.3c.4.9 1 1.5 1.9 1.9l.3-.3c.2-.3.5-.4.8-.2l1.1.6c.4.2.5.7.1 1.1-.7.8-1.6.8-2.6.2-1.2-.7-2.3-1.8-3-3-.6-1-.6-1.9.2-2.6z" fill="#58585a"/></svg>
          555-318-0472
        </li>
        <li class="contact-item">
          <svg viewBox="0 0 14 16"><path d="M7 1a5 5 0 0 0-5 5c0 3.5 5 9 5 9s5-5.5 5-9a5 5 0 0 0-5-5z" fill="none" stroke="#f5a31a" stroke-width="2"/></svg>
          Brookvale MD 20911
        </li>
        <li class="contact-item">
          <svg viewBox="0 0 14 16"><rect x="0.5" y="4" width="13" height="9" fill="#f5a31a"/><path d="M0.5 4.5 7 9.5 13.5 4.5" fill="none" stroke="#58585a" stroke-width="1"/></svg>
          Daled@voltharborcrafters.example
        </li>
      </ul>
    </div>
  </div>
</body>
</html>
```